Sub Luna Sales Flyer for Cost Accounting Business

We have a draft of a flyer that we would like to send to 200 clients. We want it to have some "pop". It should be a tri fold brochure and delivered in a format that we can work with to update as needed (verbage, not design).

This brochure could be a stand alone or attached to a letter to get clients to inquire with our firm about doing consulting work.

Target Market(s)

County Government Clients

Industry/Entity Type

Consulting

Font styles to use
Serif
Sans Serif

Colors
3176b5
33b8a4
faa54b
6b449b
0355a3

Requirements
Must have
• Clear Message
• Cover the material on the attached draft brochure that we did ourselves
• promote our logo and our message
• be colorful or something that a client will at least want to look at
• be delivered in a format that I can easily edit text, if necessary.
Nice to have
• Nice Graphics Black is another color to mix in with color. Fewer white pages.
Should not have
• my project should not be boring

```html
<!DOCTYPE html>
<html lang="en">
<head>
<meta charset="utf-8">
<title>Sub Luna Tri-Fold Brochure – Inside Spread</title>
<link rel="stylesheet" href="https://fonts.googleapis.com/css2?family=Open+Sans:ital,wght@0,400;0,700;1,400&family=Ubuntu:wght@500;700&display=swap">
<style>
  :root {
    --blue: #3176b5;
    --deep-blue: #0355a3;
    --teal: #33b8a4;
    --orange: #faa54b;
    --paper: #f7f7f7;
    --stage: #e4e6e8;
    --white: #ffffff;
  }
  * { box-sizing: border-box; margin: 0; padding: 0; }
  html, body { width: 1200px; height: 1200px; overflow: hidden; background: var(--stage); }
  .canvas { position: relative; width: 1200px; height: 1200px; }
  .brochure {
    position: absolute; left: 30px; top: 160px;
    width: 1203px; height: 930px;
    transform: scale(0.9476); transform-origin: 0 0;
    background: var(--paper); overflow: hidden;
    font-family: "Open Sans", sans-serif;
    box-shadow: 0 6px 18px rgba(0,0,0,.18);
  }
  .fold { position: absolute; top: 0; bottom: 0; width: 401px; }
  .fold--left { left: 0; background: linear-gradient(90deg, #fafafa, #f1f1f1); }
  .fold--middle { left: 401px; background: linear-gradient(90deg, #ececec, #f8f8f8 20%, #f6f6f6); }
  .fold--right { left: 802px; background: linear-gradient(90deg, #ebebeb, #f8f8f8 20%, #f6f6f6); }
  .artwork { position: absolute; inset: 0; }

  .panel-heading {
    position: absolute; height: 44px; background: var(--blue); color: var(--white);
    font-family: "Ubuntu", sans-serif; font-weight: 700; font-size: 25px;
    display: flex; align-items: center; justify-content: center;
  }
  .difference-heading { left: 44px; top: 44px; width: 314px; }
  .difference-box {
    position: absolute; left: 44px; top: 88px; width: 314px; height: 194px;
    background: var(--teal); padding: 22px 20px 0 22px; color: var(--white);
  }
  .difference-list { list-style: none; font-size: 14.3px; line-height: 16.8px; }
  .difference-list li { position: relative; padding-left: 24px; }
  .difference-list li::before {
    content: ""; position: absolute; left: 2px; top: 5px; width: 7px; height: 7px; background: var(--white);
  }

  .testimonial { position: absolute; left: 44px; top: 322px; width: 330px; color: var(--blue); }
  .testimonial .mark {
    position: absolute; font-family: "Ubuntu", sans-serif; font-weight: 700;
    font-size: 46px; color: var(--teal); line-height: 1;
  }
  .testimonial .mark--open { left: -2px; top: -4px; }
  .testimonial p { padding-left: 30px; font-size: 18px; line-height: 20px; }
  .testimonial .close { color: var(--teal); font-family: "Ubuntu", sans-serif; font-weight: 700; font-size: 38px; line-height: 0; vertical-align: -12px; }

  .middle-copy { position: absolute; left: 445px; top: 44px; width: 314px; color: var(--blue); }
  .section-title { font-family: "Ubuntu", sans-serif; font-weight: 500; font-size: 22px; margin-bottom: 12px; }
  .middle-copy p { font-size: 14.5px; line-height: 16.8px; text-align: justify; margin-bottom: 17px; }
  .middle-copy .section-title--tools { margin-top: 40px; }

  .team-heading { left: 846px; top: 44px; width: 313px; }
  .team-box {
    position: absolute; left: 846px; top: 88px; width: 313px; height: 760px;
    background: var(--teal); color: var(--white); padding: 22px 21px 0 21px;
  }
  .team-box p { font-size: 14.4px; line-height: 16.8px; text-align: justify; margin-bottom: 16.5px; }
  .team-box strong { font-weight: 700; }

  .web-strip {
    position: absolute; left: 820px; top: 871px; width: 383px; height: 59px;
    color: var(--white); font-weight: 700; font-size: 14.5px;
    display: flex; align-items: center; justify-content: flex-end; padding-right: 42px;
  }
</style>
</head>
<body>
<div class="canvas">
  <div class="brochure">
    <div class="fold fold--left"></div>
    <div class="fold fold--middle"></div>
    <div class="fold fold--right"></div>

    <svg class="artwork" viewBox="0 0 1203 930" width="1203" height="930">
      <defs>
        <linearGradient id="officeTones" x1="0" y1="0" x2="1" y2="1">
          <stop offset="0" stop-color="#9eb3c9"/>
          <stop offset="0.35" stop-color="#dfe6ee"/>
          <stop offset="0.7" stop-color="#c7d2de"/>
          <stop offset="1" stop-color="#8fa3ba"/>
        </linearGradient>
      </defs>
      <rect role="img" aria-label="Photo of a team of consultants reviewing documents around an office table" x="0" y="470" width="1203" height="460" fill="url(#officeTones)"/>
      <path d="M0,505 C260,600 560,625 846,560 C960,534 1090,505 1203,490 L1203,470 C1090,488 960,516 846,540 C560,600 260,580 0,490 Z" fill="var(--deep-blue)"/>
      <path d="M0,445 C240,520 500,545 846,520 C960,508 1090,470 1203,450 L1203,472 C1090,488 960,514 846,535 C560,592 260,572 0,482 Z" fill="var(--teal)"/>
      <path d="M0,520 C260,610 560,630 846,565 C960,540 1090,512 1203,500 L1203,930 L0,930 Z" fill="url(#officeTones)" role="img" aria-label="Photo continued"/>
      <path d="M0,500 C260,590 560,615 846,552 C960,528 1090,500 1203,488 L1203,500 C1090,512 960,540 846,565 C560,630 260,610 0,520 Z" fill="var(--deep-blue)"/>
      <polygon points="838,871 1203,871 1203,930 805,930" fill="var(--blue)"/>
      <polygon points="826,871 838,871 805,930 793,930" fill="var(--orange)"/>
      <polygon points="838,871 852,871 819,930 805,930" fill="var(--orange)"/>
    </svg>

    <div class="panel-heading difference-heading">The Sub Luna Difference</div>
    <div class="difference-box">
      <ul class="difference-list">
        <li>We will save you as much as 30% over our competitor pricing.</li>
        <li>You get the most qualified individuals working directly for you.</li>
        <li>Produced with our proprietary, state of the art, .NET system.</li>
        <li>Built in analysis tools.</li>
        <li>Automatically produces the plan in PDF and EXCEL formats.</li>
      </ul>
    </div>

    <blockquote class="testimonial">
      <span class="mark mark--open">&ldquo;</span>
      <p>Sub Luna gave our plan a fresh look and found additional recoveries that weren't in our old plan. We love the EXCEL format of the plan. - <em>Sub Luna Client</em> <span class="close">&rdquo;</span></p>
    </blockquote>

    <div class="middle-copy">
      <h2 class="section-title">Analysis</h2>
      <p>Each plan undergoes a rigorous review with our automated tools that automatically compares the proposed plan to historical numbers and looks for changes, trends and points of discussion.</p>
      <p>Receiving departments go through a three step review. First we review the receiving departments in total, second we review by central service and finally we look at changes by activity.</p>
      <h2 class="section-title section-title--tools">Our Tools</h2>
      <p>We have our own, proprietary cost allocation system. It is a .NET system and it can produce an excel version of the cost plan. In addition, we have built in analysis with every plan that will provide some detail. Our tools provide the consultant with feedback as the plan is being constructed so that they know immediately where to ask questions or for more information</p>
    </div>

    <div class="panel-heading team-heading">Our Team</div>
    <div class="team-box">
      <p><strong>Marla Venwick</strong> is a PMP and has over 25 years of consulting experience with County, City and State Agencies. I began my career in Ohio, where I did cost plans for 10 years. My project management background means that every project is scheduled, timed, and quality checked.</p>
      <p><strong>Tessa Orlund</strong> is a CPA with years of State, County and City experience. She has completed over 40 State Cost Plans and over 50 County Cost Plans. Her experience is primarily in Ohio.</p>
      <p><strong>Gwen Stalder</strong> is a CPA with 10 years of experience working with County and State Agencies in North Dakota, Minnesota and Nebraska. She brings a wealth of knowledge to the table.</p>
      <p><strong>Carly Voss</strong> has five years of experience working with cost plans in MN, ND, NE, IA and WI. She brings her expertise and experience to help us as we continue to grow.</p>
      <p><strong>Neil Farrow</strong> is located in Columbus, OH and has over 25 years of cost accounting, cost plans, and systems design work on cost accounting and timekeeping systems. Neil wrote the original PAX, CoRT and RLS systems for Ohio Human Service Agencies. He provides the technical resources for this project.</p>
      <p><strong>Owen Venwick</strong> is located in Stillwater, MN. He has a JD from St. Aldric University and a BA from Harwell College. He brings his background in cost accounting and legal experience to our group.</p>
    </div>

    <div class="web-strip">www.sublunaconsulting.com</div>
  </div>
</div>
</body>
</html>
```